GuardLume website design #1 alarm company in Arizona and California

Alarm company, home security, home protection, video, home automation, smart home, we protect family we the highest quality security products in the market with 24 hour montrioning, also allow family's to control their whole house by being everywhere in the world.

In short, we’re professional, experienced and have the necessary know-how to optimally secure your home or business. Add those skills with our commitment to service and saving you money, and you can’t go wrong trusting

Looking to have a website for current customers and future customers and current employees and future employees to go to. Target current markets listed below get a lot of leads of the website.

Target Market(s)

Arizona and California, Phoenix, Mesa,Gilbert, casa grande, Arizona city, Glendale, peoria, Goodyear, Scottsdale, fountain hills, apache junction, Tempe, surprise, anthem, buckeye, Tucson, Northern California, Modesto, Fresno, Stockton, San Jose, Manteca, Tracy, Sacramento, concord, Southern California, San Bernardino, riverside, Anaheim, Los Angeles, palm desert, Bakersfield

Industry/Entity Type

Security

Coding

Coded - Design and coding required

Number of Pages Required

5+ page

Font styles to use
Sans Serif

Colors
ec1f27
f59296
ffffff
000000
b2b2b2
cacaca
fbd4d5

Requirements
Must have
• A place where a customer can put in the info to get a system(get a free quote),a link to all of my socal media sites, a work for us page, about us page, equipment page, packages page, security page, cameras page, smart home page, support page(FAQ http://www.brightvalehome.example/faq)somthing like the alomost every answer is right. Partners page.
Nice to have
• Quorlan.example, very nicely done make it look nice like this.
• Brightvalehome.example
• Pemby.example
• Tulsix.example
• Sentravox9.example
• Wexmoresecurity.example
• These are all my favorite sites would love for it to look like this sites.
Should not have
• Need to be clean cut and sharp looking, no unnecessary stuff in it.

```html
<!DOCTYPE html>
<html lang="en">
<head>
<meta charset="utf-8">
<title>GuardLume — Home Security</title>
<link href="https://fonts.googleapis.com/css2?family=Lato:wght@400;700;900&display=swap" rel="stylesheet">
<style>
:root{
  --red:#ec1f27;
  --pink:#f59296;
  --blush:#fbd4d5;
  --white:#ffffff;
  --black:#000000;
  --ink:#3a3a3a;
  --muted:#8a8a8a;
  --soft:#b2b2b2;
  --line:#cacaca;
  --panel:#f2f2f2;
  --steel:#7a7a7a;
  --foot:#7b7b7b;
  --foot-low:#a9a9a9;
}
*{box-sizing:border-box;margin:0;padding:0}
html,body{width:1200px;height:2853px;overflow:hidden}
body{font-family:'Lato',Arial,sans-serif;color:var(--ink);background:var(--white);position:relative}
section,header,footer{position:relative;width:1200px;overflow:hidden}
.abs{position:absolute}
.btn{position:absolute;background:var(--red);color:var(--white);font-weight:700;font-size:11px;letter-spacing:.3px;display:flex;align-items:center;justify-content:center;text-transform:uppercase}
.ph{position:absolute}

/* header */
.site-header{height:76px;background:var(--white);box-shadow:0 2px 4px rgba(0,0,0,.12);z-index:2}
.brand{position:absolute;left:162px;top:24px;display:flex;align-items:center;gap:8px}
.brand-mark{width:20px;height:20px;background:var(--red)}
.brand-name{font-weight:900;font-size:20px;color:var(--ink)}
.nav{position:absolute;left:521px;top:28px;display:flex;gap:24px;font-size:12.5px;color:var(--muted)}

/* hero */
.hero{height:337px}
.hero-photo{left:0;top:0;width:1200px;height:337px;background:linear-gradient(90deg,#ffffff 0%,#f7f4f0 30%,#e6d6c4 55%,#c7a58a 75%,#8a9e7a 100%)}
.hero-title{left:162px;top:86px;font-size:27px;line-height:34px;font-weight:900;color:var(--red);width:480px;text-transform:uppercase}
.hero-sub{left:162px;top:162px;font-size:14.5px;line-height:20px;font-weight:700;color:#555;width:340px;text-transform:uppercase}
.hero .btn{left:162px;top:223px;width:89px;height:28px}

/* services */
.services{height:224px;border-bottom:1px solid #e5e5e5}
.service{position:absolute;top:38px;width:150px;text-align:center}
.service svg{display:block;margin:0 auto;width:52px;height:52px}
.service h3{margin-top:26px;font-size:14px;font-weight:700;color:#555}
.service p{margin-top:10px;font-size:10px;line-height:15px;color:var(--soft)}

/* customer service */
.care{height:301px;background:var(--panel)}
.care h2{left:168px;top:52px;font-size:18px;line-height:26px;font-weight:700;color:#444;width:360px;text-transform:uppercase}
.care p{left:168px;top:119px;font-size:11.5px;line-height:17px;color:#666;width:425px}
.care .btn{left:168px;top:202px;width:89px;height:29px}
.care-device{left:624px;top:52px;width:396px;height:190px;border-radius:28px;background:#151515;padding:12px 58px}
.care-device div{width:100%;height:100%;background:linear-gradient(135deg,#cfc6b8,#9a8a79 55%,#6b5d52)}

/* control ways */
.ways{height:224px}
.ways h2{left:162px;top:70px;font-size:16px;line-height:21px;font-weight:700;color:#555;text-transform:uppercase}
.ways p{left:162px;top:120px;font-size:11px;line-height:16px;color:var(--muted);width:220px}
.product-label{position:absolute;font-size:10.5px;font-weight:700;color:#555;text-transform:uppercase;text-align:center;width:160px}
.device{position:absolute}

/* quote */
.quote{height:339px}
.quote-photo{left:0;top:0;width:666px;height:339px;background:linear-gradient(90deg,#e4e4e4,#f1f1f1 55%,#e9e9e9)}
.quote-panel{left:666px;top:0;width:372px;height:339px;background:#f4f4f4}
.quote-edge{left:1038px;top:0;width:162px;height:339px;background:linear-gradient(90deg,#2b2b2b,#141414)}
.quote h2{left:666px;top:52px;width:372px;text-align:center;font-size:26px;font-weight:400;color:#555;text-transform:uppercase}
.quote h2 span{color:var(--red)}
.field{position:absolute;left:717px;width:276px;height:36px;background:var(--white);border:1px solid #e3e3e3;display:flex;align-items:center;padding-left:12px;gap:8px;font-size:10px;color:var(--soft)}
.field svg{width:11px;height:11px}
.quote .btn{left:717px;top:244px;width:276px;height:34px;font-size:11.5px}

/* packages */
.packages{height:224px}
.packages h2{left:162px;top:70px;font-size:16px;line-height:21px;font-weight:700;color:#555;text-transform:uppercase}
.packages p{left:162px;top:120px;font-size:11px;line-height:16px;color:var(--muted);width:220px}
.packages .product-label.active{color:var(--red)}

/* install */
.install{height:301px}
.install-photo{left:0;top:0;width:601px;height:301px;background:linear-gradient(90deg,#c9d8e4,#9c8272 45%,#8b5a42 75%,#a0705a)}
.install-panel{left:601px;top:0;width:599px;height:301px;background:var(--steel)}
.install h2{left:633px;top:78px;font-size:20px;line-height:26px;font-weight:700;color:var(--white);text-transform:uppercase}
.install p{left:633px;top:152px;font-size:13px;line-height:20px;color:var(--white);width:270px}

/* carousel */
.carousel{height:224px;background:#f5f5f5}
.arrow{position:absolute;top:76px;width:28px;height:72px}
.carousel .product-label{top:174px;color:#666;font-weight:400;font-size:10px}

/* info */
.info{height:299px}
.info h4{position:absolute;top:36px;font-size:16px;font-weight:400;color:#555;text-transform:uppercase}
.offer-item{position:absolute;left:177px;display:flex;align-items:center;gap:12px;font-size:10px;color:#777;text-transform:uppercase}
.offer-item svg{width:26px;height:26px}
.offer-item.active{color:#333;font-weight:700}
.feature-list{position:absolute;left:468px;top:75px;width:270px;list-style:none}
.feature-list li{height:30px;border-bottom:1px solid #dcdcdc;font-size:11px;color:#777;display:flex;align-items:center;padding-left:2px}
.about-text{left:791px;top:88px;width:250px;font-size:13px;line-height:22px;color:#666}
.info .btn{left:791px;top:215px;width:90px;height:28px}

/* footer */
.site-footer{height:266px;background:var(--foot)}
.foot-brand{left:224px;top:62px;width:150px;text-align:center}
.foot-brand .mark{width:34px;height:34px;background:var(--white);margin:0 auto 6px}
.foot-brand .name{font-weight:900;font-size:17px;color:var(--white);text-transform:uppercase}
.socials{left:236px;top:133px;display:flex;gap:6px}
.socials span{width:26px;height:26px;border:1px solid var(--white);display:block}
.foot-col h5{position:absolute;font-size:13px;font-weight:700;color:var(--white);text-transform:uppercase}
.foot-links{position:absolute;list-style:none;font-size:11.5px;color:var(--white)}
.foot-links li{height:19.5px}
.copyright{height:38px;background:var(--foot-low);color:var(--white);font-size:11.5px;display:flex;align-items:center;justify-content:center}
</style>
</head>
<body>

<header class="site-header">
  <div class="brand"><span class="brand-mark"></span><span class="brand-name">GuardLume</span></div>
  <nav class="nav"><span>Home Page</span><span>About us</span><span>Equipment &amp; Packages</span><span>Security &amp; Cameras</span><span>Smart Home</span><span>Support</span></nav>
</header>

<section class="hero">
  <div class="ph hero-photo" role="img" aria-label="Photo of a smiling family of four outside their home"></div>
  <h1 class="abs hero-title">We protect family we highest quality security</h1>
  <p class="abs hero-sub">Products in the market with 24 hour montrioning</p>
  <span class="btn">Read more</span>
</section>

<section class="services">
  <div class="service" style="left:166px">
    <svg viewBox="0 0 52 52"><path d="M26 4 L44 11 V25 C44 37 36 45 26 49 C16 45 8 37 8 25 V11 Z" fill="none" stroke="#1f6fb8" stroke-width="3"/><circle cx="26" cy="26" r="8" fill="none" stroke="#1f6fb8" stroke-width="3"/><circle cx="26" cy="26" r="3" fill="#1f6fb8"/></svg>
    <h3>SECURITY</h3><p>we protect family we the highest quality security products in the market with 24 hour</p>
  </div>
  <div class="service" style="left:345px">
    <svg viewBox="0 0 52 52"><path d="M26 5 C16 5 11 13 11 20 C11 28 18 31 19 38 H33 C34 31 41 28 41 20 C41 13 36 5 26 5 Z" fill="none" stroke="#f0693a" stroke-width="3"/><path d="M20 43 H32 M22 48 H30" stroke="#f0693a" stroke-width="3"/></svg>
    <h3>ENERGY</h3><p>we protect family we the highest quality security products in the market with 24 hour</p>
  </div>
  <div class="service" style="left:526px">
    <svg viewBox="0 0 52 52"><path d="M3 18 L26 5 L49 18 V48 H3 Z" fill="#2e9a5a"/><rect x="11" y="22" width="30" height="26" fill="#fff"/><path d="M11 27 H41 M11 32 H41 M11 37 H41 M11 42 H41" stroke="#2e9a5a" stroke-width="2.5"/></svg>
    <h3>HOME AUTOMATION</h3><p>we protect family we the highest quality security products in the market with 24 hour</p>
  </div>
  <div class="service" style="left:703px">
    <svg viewBox="0 0 52 52"><circle cx="17" cy="17" r="11" fill="#f08a8e"/><circle cx="14" cy="14" r="3.5" fill="#fff"/><path d="M24 24 L44 44 L40 48 L36 44 L39 41 L35 37 L32 40 L28 36" fill="#f08a8e"/></svg>
    <h3>ACCESS</h3><p>we protect family we the highest quality security products in the market with 24 hour</p>
  </div>
  <div class="service" style="left:882px">
    <svg viewBox="0 0 52 52"><path d="M6 12 L38 12 L42 24 L10 24 Z" fill="none" stroke="#b5732e" stroke-width="3"/><path d="M42 16 L50 12 V26 L42 22" fill="#b5732e"/><path d="M22 24 V34 H8 M8 28 V40" stroke="#b5732e" stroke-width="3" fill="none"/></svg>
    <h3>VIDEO</h3><p>we protect family we the highest quality security products in the market with 24 hour</p>
  </div>
</section>

<section class="care">
  <h2 class="abs">Get real customer service that respects your time!</h2>
  <p class="abs">We protect family we the highest quality security products in the market with 24 hour montrioning, also allow family's to control their whole house by being everywhere in the world.We protect family we the highest quality security products in the market with 24 hour montrioning.</p>
  <span class="btn">Read more</span>
  <div class="ph care-device" role="img" aria-label="Smartphone showing a live front door camera view"><div></div></div>
</section>

<section class="ways">
  <h2 class="abs">Three ways to<br>control your home</h2>
  <p class="abs">We protect family we the highest quality security products</p>
  <div class="device" role="img" aria-label="Wall-mounted home control panel" style="left:434px;top:64px;width:106px;height:80px;background:linear-gradient(160deg,#f4f4f4,#d2d2d2);border-radius:6px"></div>
  <div class="device" role="img" aria-label="Smartphone with security app" style="left:662px;top:90px;width:103px;height:52px;background:#1b1b1b;border-radius:8px"></div>
  <div class="device" role="img" aria-label="Smartwatch with security app" style="left:905px;top:40px;width:65px;height:106px;background:linear-gradient(#bdbdbd,#2a2a2a 30%,#2a2a2a 70%,#bdbdbd);border-radius:12px"></div>
  <span class="product-label" style="left:407px;top:162px">Home control</span>
  <span class="product-label" style="left:631px;top:162px">Mobile control</span>
  <span class="product-label" style="left:858px;top:162px">Watch control</span>
</section>

<section class="quote">
  <div class="ph quote-photo" role="img" aria-label="Video doorbell mounted on a white wall"></div>
  <div class="abs quote-panel"></div>
  <div class="ph quote-edge" role="img" aria-label="Dark door frame"></div>
  <h2 class="abs">Get a free <span>quote</span></h2>
  <div class="field" style="top:107px"><svg viewBox="0 0 12 12"><circle cx="6" cy="3.5" r="2.8" fill="#999"/><path d="M1 12 C1 8 11 8 11 12Z" fill="#999"/></svg>Full Name</div>
  <div class="field" style="top:145px"><svg viewBox="0 0 12 12"><rect x="3" y="0.5" width="6" height="11" rx="1" fill="none" stroke="#999"/></svg>Phone Number</div>
  <div class="field" style="top:183px"><svg viewBox="0 0 12 12"><rect x="0.5" y="2" width="11" height="8" fill="none" stroke="#999"/><path d="M0.5 2 L6 7 L11.5 2" fill="none" stroke="#999"/></svg>Email</div>
  <span class="btn">Request a quote</span>
</section>

<section class="packages">
  <h2 class="abs">Secure mobile<br>package</h2>
  <p class="abs">We protect family we the highest quality security products</p>
  <div class="device" role="img" aria-label="Control panel with smartphone" style="left:434px;top:93px;width:99px;height:51px;background:linear-gradient(90deg,#e2e2e2 65%,#1b1b1b 65%);border-radius:4px"></div>
  <div class="device" role="img" aria-label="Control panel with keypad lock" style="left:666px;top:93px;width:99px;height:51px;background:linear-gradient(90deg,#e2e2e2 65%,#2a2a2a 65%);border-radius:4px"></div>
  <div class="device" role="img" aria-label="Control panel with smartwatch" style="left:890px;top:93px;width:99px;height:51px;background:linear-gradient(90deg,#e2e2e2 65%,#3a3a3a 65%);border-radius:4px"></div>
  <span class="product-label" style="left:403px;top:163px">Secure mobile</span>
  <span class="product-label active" style="left:635px;top:163px">Secure control</span>
  <span class="product-label" style="left:859px;top:163px">Secure watch</span>
</section>

<section class="install">
  <div class="ph install-photo" role="img" aria-label="Technician installing a security camera on a brick wall"></div>
  <div class="abs install-panel"></div>
  <h2 class="abs">Free professional<br>installation*</h2>
  <p class="abs">We protect family we the highest quality security products in the market with 24 hour montrioning.</p>
</section>

<section class="carousel">
  <svg class="arrow" style="left:161px" viewBox="0 0 28 72"><path d="M26 2 L3 36 L26 70" fill="none" stroke="#b2b2b2" stroke-width="2"/></svg>
  <svg class="arrow" style="left:1011px" viewBox="0 0 28 72"><path d="M2 2 L25 36 L2 70" fill="none" stroke="#ec1f27" stroke-width="2"/></svg>
  <div class="device" role="img" aria-label="Security camera" style="left:222px;top:38px;width:92px;height:118px;background:linear-gradient(#ffffff,#d8d8d8);border-radius:8px"></div>
  <div class="device" role="img" aria-label="Security smartwatch" style="left:400px;top:44px;width:72px;height:110px;background:linear-gradient(#c4c4c4,#222 30%,#222 70%,#c4c4c4);border-radius:12px"></div>
  <div class="device" role="img" aria-label="Security app on smartphone" style="left:568px;top:40px;width:54px;height:112px;background:#1a1a1a;border-radius:8px"></div>
  <div class="device" role="img" aria-label="Keypad door lock" style="left:720px;top:40px;width:74px;height:114px;background:linear-gradient(#3a3a3a,#111);border-radius:30px"></div>
  <div class="device" role="img" aria-label="Video doorbell" style="left:860px;top:40px;width:114px;height:114px;background:radial-gradient(circle,#777 20%,#cfcfcf 60%,#a5a5a5);border-radius:50%"></div>
  <span class="product-label" style="left:188px">Security camera</span>
  <span class="product-label" style="left:356px">Security watch</span>
  <span class="product-label" style="left:515px">Security mobile</span>
  <span class="product-label" style="left:677px">Security lock</span>
  <span class="product-label" style="left:837px">Security bell</span>
</section>

<section class="info">
  <h4 style="left:177px">What we offer</h4>
  <h4 style="left:468px">Our feactures</h4>
  <h4 style="left:791px">About us</h4>

  <div class="offer-item" style="top:73px"><svg viewBox="0 0 26 26"><path d="M13 2 L22 6 V13 C22 19 18 22 13 24 C8 22 4 19 4 13 V6 Z" fill="none" stroke="#bbb" stroke-width="1.6"/></svg>Security</div>
  <div class="offer-item active" style="top:113px"><svg viewBox="0 0 26 26"><path d="M13 2 C8 2 5 6 5 10 C5 14 9 16 9 19 H17 C17 16 21 14 21 10 C21 6 18 2 13 2Z" fill="none" stroke="#ec1f27" stroke-width="2"/><path d="M10 22 H16" stroke="#ec1f27" stroke-width="2"/></svg>Energy</div>
  <div class="offer-item" style="top:152px"><svg viewBox="0 0 26 26"><path d="M2 9 L13 3 L24 9 V24 H2Z" fill="#c4c4c4"/><rect x="6" y="11" width="14" height="13" fill="#fff"/><path d="M6 14 H20 M6 17 H20 M6 20 H20" stroke="#c4c4c4"/></svg>Home automation</div>
  <div class="offer-item" style="top:192px"><svg viewBox="0 0 26 26"><circle cx="9" cy="9" r="6" fill="#c4c4c4"/><path d="M12 12 L23 23 L21 25 L12 16" fill="#c4c4c4"/></svg>Access</div>
  <div class="offer-item" style="top:232px"><svg viewBox="0 0 26 26"><path d="M3 7 H18 L20 13 H5Z" fill="none" stroke="#bbb" stroke-width="1.6"/><path d="M11 13 V18 H4 M4 15 V21" stroke="#bbb" stroke-width="1.6" fill="none"/></svg>Video</div>

  <ul class="feature-list">
    <li>Touch screen control panel</li>
    <li>Motion detector</li>
    <li>Door/window sensor</li>
    <li>Glass break detector</li>
    <li>Remote web and mobile access</li>
    <li>Two-way voice featur</li>
  </ul>

  <p class="abs about-text">We protect family we the highest quality security products in the market with 24 hour montrioning, also allow family's to control their whole house by being everywhere in the world.</p>
  <span class="btn">Read more</span>
</section>

<footer class="site-footer">
  <div class="abs foot-brand"><div class="mark"></div><div class="name">GuardLume</div></div>
  <div class="abs socials"><span></span><span></span><span></span><span></span></div>
  <div class="foot-col">
    <h5 style="left:460px;top:62px">Company</h5>
    <ul class="foot-links" style="left:460px;top:92px"><li>About us</li><li>Packages</li><li>Cameras</li><li>Support</li></ul>
    <ul class="foot-links" style="left:542px;top:92px"><li>Equipment</li><li>Security</li><li>Smart Home</li></ul>
  </div>
  <div class="foot-col">
    <h5 style="left:761px;top:62px">Company</h5>
    <ul class="foot-links" style="left:761px;top:92px;font-size:11px">
      <li>Touch screen control panel</li><li>Motion detector</li><li>Door/window sensor</li><li>Glass break detector</li><li>Remote web and mobile access</li><li>Two-way voice featur</li>
    </ul>
  </div>
</footer>
<div class="copyright">Copyright © 2016 GuardLume. All rights reserved</div>

</body>
</html>
```